Gestaltung Flyer & Infokärtchen für Tellerbund
Zielgruppe
Hungrige Personen im Geschäft/Firma (keine Privatpersonen zu Hause), welche Menüs bestellen wollen. Die Menüs dürfen nicht zuviel kosten, aber der Flyer darf deshalb auch nicht "billig" daher kommen. Im Gegenteil.
Aufgabenstellung
Tellerbund - Deine Food Community ist eine seite, die virtuelle Bestellgemeinschaften schafft und damit Lieferpauschalen und Mindestbestellmengen für den Einzelbesteller umgeht. Der Einzelbesteller kennt also seine "Mitbesteller" nicht. Zudem wird das Menü günstiger, je mehr Leute in seiner Community bestellen. Diese Mitbesteller sind andere Personen in der gleichen Firma oder direkte Nachbarfirmen. In jedem Fall geht es um Bestellung von warmen Menüs.
Enorm wichtig und absolut zentral bei dem Infoflyer A4 UND dem kleinen Infokärtchen (A6 gefaltet mit aussen hinten weiss, aussen vorne Hauptmessage mit Logo (seperater Wettbewerb) und Innen zentrale Messages mit Internetseite www.TBM.ch) ist:
1. Der zentrale Unterschied zu anderen Bestellsystemen. warum der Kunde bei uns bestellen soll. Aus 2 Gründen!
1. "Keine Lieferpauschale", "Keine Mindestbestellmenge", "Punkte sammeln". Keine Lieferpauschale und keine Mindestbestellmenge - auch wenn nur 1 Menü bestellt wird. Bei Jedem Kauf kann der Besteller Punkte sammeln und diese dann in gratis Menü umwandeln. Zudem sammelt auch die virtuelle Bestellgemeinschaft punkte. Bei Erreichen von xy Punkten wird in der Community Preise verlost.
2. Community Gedanke: Je mehr bestellt wird, desto günstiger wird der Preis - bis zu einem bestimmten Minimum. Bei ersten Besteller kostet also bspw. das Menü warm geliefert all inkl. 15 Euro; bis minimum 9 Euro. Es muss aber voraus bezahlt werden (diese info muss aber ncht unbedingt auch drauf).
Beispiele für den Community Gedanken wären:
- "Tellerbund - Deine Food Community - Je mehr bestellen, desto günstiger wird’s"
- "Tellerbund - Deine Food Community - Andere bestellen - Du profitierst"
- "Tellerbund - Deine Food Community - Du bist teil der Community - mehr Besteller - günstiger Preis" etc.
- oder man stellt dies bildlich dar zusammen bspw. mit text 1 (ich stelle mir bspw. vor, 1 männchen hoher Preis ($ oben auf berg) und..

```html
<!DOCTYPE html>
<html lang="de">
<head>
<meta charset="utf-8">
<title>Tellerbund – Flyer</title>
<link rel="stylesheet" href="https://fonts.googleapis.com/css2?family=PT+Sans:wght@400;700&family=Fira+Sans+Condensed:wght@600&display=swap">
<style>
  :root{
    --page:#ffffff;
    --frame:#e27a12;
    --sky-top:#d9e9f3;
    --sky-bottom:#ffffff;
    --headline:#4f87c2;
    --benefit:#e07814;
    --button-top:#e3f0b8;
    --button-bottom:#a9cc5e;
    --button-text:#ffffff;
    --url:#3f6fa3;
    --plate:#f7f7f7;
    --icon:#5a5a5a;
  }
  *{margin:0;padding:0;box-sizing:border-box}
  html,body{width:1200px;height:1200px;overflow:hidden;background:var(--page)}
  .flyer{
    position:absolute;left:205px;top:46px;width:789px;height:1107px;
    background:var(--frame);overflow:hidden;
  }
  .flyer-panel{
    position:absolute;left:12px;top:12px;right:12px;bottom:12px;
    border-radius:16px;overflow:hidden;
    background:linear-gradient(180deg,var(--sky-top) 0%,#eaf3f8 45%,var(--sky-bottom) 100%);
  }
  .bubble-field{
    position:absolute;left:0;top:0;width:100%;height:560px;
    background:
      radial-gradient(circle at 18% 12%,rgba(255,255,255,.55) 0 60px,transparent 62px),
      radial-gradient(circle at 40% 24%,rgba(255,255,255,.45) 0 48px,transparent 50px),
      radial-gradient(circle at 10% 34%,rgba(255,255,255,.4) 0 36px,transparent 38px),
      radial-gradient(circle at 70% 60%,rgba(255,255,255,.4) 0 34px,transparent 36px),
      radial-gradient(circle at 55% 82%,rgba(255,255,255,.35) 0 26px,transparent 28px);
  }
  .plate{
    position:absolute;left:286px;top:-365px;width:700px;height:700px;border-radius:50%;
    background:var(--plate);box-shadow:0 2px 6px rgba(0,0,0,.08);
  }
  .brand{
    position:absolute;left:480px;top:78px;display:flex;align-items:center;gap:14px;
  }
  .brand-dot{width:38px;height:38px;border-radius:50%;background:var(--frame)}
  .brand-name{
    font-family:"PT Sans",sans-serif;font-weight:700;font-size:34px;
    color:var(--frame);letter-spacing:.5px;
  }
  .headline{
    position:absolute;left:99px;top:305px;
    font-family:"PT Sans",sans-serif;font-weight:400;color:var(--headline);
    line-height:1;
  }
  .headline-line{display:block;font-size:34px;white-space:nowrap}
  .headline-line + .headline-line{margin-top:10px;padding-left:18px}
  .headline strong{font-weight:700;font-size:66px;letter-spacing:-.5px}
  .benefits{
    position:absolute;left:50px;top:536px;list-style:none;
    font-family:"Fira Sans Condensed",sans-serif;font-weight:600;
    font-size:26px;color:var(--benefit);
  }
  .benefits li{display:flex;align-items:center;gap:14px;height:53px}
  .benefits svg{width:28px;height:28px}
  .cta{
    position:absolute;left:92px;top:723px;width:247px;height:63px;border-radius:10px;
    background:linear-gradient(180deg,var(--button-top),var(--button-bottom));
    box-shadow:0 3px 6px rgba(0,0,0,.25);
    font-family:"PT Sans",sans-serif;font-size:29px;color:var(--button-text);
    display:flex;align-items:center;justify-content:center;
    text-shadow:0 1px 2px rgba(0,0,0,.2);
  }
  .cta-pointer{position:absolute;left:294px;top:772px;width:34px;height:48px}
  .pointer-crowd{
    position:absolute;left:324px;top:806px;width:453px;height:289px;
    background:linear-gradient(160deg,#f4f6f8,#dfe3e7);
    clip-path:polygon(60% 0,100% 5%,100% 100%,0 100%,2% 70%,30% 30%);
  }
  .site-url{
    position:absolute;left:50px;top:1030px;
    font-family:"PT Sans",sans-serif;font-weight:700;font-size:25px;color:var(--url);
  }
</style>
</head>
<body>
  <main class="flyer">
    <div class="flyer-panel">
      <div class="bubble-field" role="img" aria-label="Schwebende, durchscheinende Blasen mit Minus-CHF-Zeichen"></div>
      <div class="plate"></div>
      <div class="brand">
        <span class="brand-dot"></span>
        <span class="brand-name">TELLERBUND</span>
      </div>

      <h1 class="headline">
        <span class="headline-line">Je <strong>mehr</strong> bestellen,</span>
        <span class="headline-line">desto <strong>günstiger</strong> wird’s</span>
      </h1>

      <ul class="benefits">
        <li><svg viewBox="0 0 28 28"><circle cx="14" cy="14" r="12" fill="none" stroke="var(--icon)" stroke-width="2"/><path d="M8 14.5l4 4 8-9" fill="none" stroke="var(--icon)" stroke-width="2.5" stroke-linecap="round" stroke-linejoin="round"/></svg>Keine Mindestbestellung</li>
        <li><svg viewBox="0 0 28 28"><circle cx="14" cy="14" r="12" fill="none" stroke="var(--icon)" stroke-width="2"/><path d="M8 14.5l4 4 8-9" fill="none" stroke="var(--icon)" stroke-width="2.5" stroke-linecap="round" stroke-linejoin="round"/></svg>Keine Lieferpauschal</li>
        <li><svg viewBox="0 0 28 28"><circle cx="14" cy="14" r="12" fill="none" stroke="var(--icon)" stroke-width="2"/><path d="M8 14.5l4 4 8-9" fill="none" stroke="var(--icon)" stroke-width="2.5" stroke-linecap="round" stroke-linejoin="round"/></svg>Essen und Punkte sammeln</li>
      </ul>

      <div class="cta">jetzt sparen</div>
      <svg class="cta-pointer" viewBox="0 0 34 48"><path d="M3 3v36l9-8 7 14 6-3-7-14h12z" fill="#fff" stroke="#222" stroke-width="2.5" stroke-linejoin="round"/></svg>

      <div class="pointer-crowd" role="img" aria-label="Viele Mauszeiger, die sich zur Ecke hin häufen"></div>

      <p class="site-url">www.tellerbund.ch</p>
    </div>
  </main>
</body>
</html>
```